Greyfield Ridge Medical Website to make connecting and communicating easier

To create a unique, user-friendly, professional website for patients and professionals to access education/ information, forms, appointments, contact details, and data about us, and for us to have the capacity to link to various cloud-based platforms.
To use the logo design and colour scheme we have just sourced.

WEBSITE to be eye catching, Inspiring and alluring
- efficient and logical
- professional and trustworthy appearance
- health focus "living health matters"
- user friendly
- ability to link with cloud-based software and video conferencing tools/ telehealth
- colours- black/ white teal and ?silver

PAGES:
page 1 - Our clinic and staff, services offered, contact us- address/ map / contact details- social media connections
page 2- patients and visitors - New patient forms to complete, news and patient informtion (educatinal)
page 3 - health professionals -referral forms, research and education
page 3- online appointments
page 4 - Quick links - partners, other services
page 5- privacy policy, disclaimer

HI, Could we please extend the deadline another 5 days, so sorry just struggling with my workload to be able to keep up and I am wanting to liaise more with the designer that I will choose. I am so happy with PixelHarbor and all the designers - thank you! Thank you so much!!

Target Market(s)

Patients - mostly over 60's so the website must be minimal clicks and simple to navigate
Professionals - for education and access forms

Industry/Entity Type

Health Care

Coding

Coded - Design and coding required

Number of Pages Required

5+ page

Font styles to use
Sans Serif
Script

Colors
33b8a4
86cfc6

Requirements
Must have
• WEBSITE to be eye catching, Inspiring and alluring
- efficient and logical
- user friendly

WEBSITE - professional and user friendly
- ability to link with cloud based software and videoconferencing/ telehealth
Nice to have
• clean and crisp presentation
happy for an innovative look
room to add more services and ability to link pages and resources
Should not have
• Please ensure the website is not:
clunky
difficult to navigate
common and cheap looking

```html
<!DOCTYPE html>
<html lang="en">
<head>
<meta charset="utf-8">
<title>Greyfield Ridge Medical</title>
<link href="https://fonts.googleapis.com/css2?family=Poppins:wght@300;400;500;600;700;800&display=swap" rel="stylesheet">
<style>
:root{
  --teal:#33b8a4;
  --teal-dark:#2aa391;
  --teal-light:#86cfc6;
  --ink:#1e1e1e;
  --text:#555;
  --muted:#9a9a9a;
  --grey:#efefef;
  --line:#e6e6e6;
  --white:#fff;
}
*{box-sizing:border-box;margin:0;padding:0}
html,body{width:1200px;height:3971px;overflow:hidden}
body{position:relative;font-family:'Poppins',sans-serif;color:var(--text);background:var(--white)}
.abs{position:absolute}
p{font-size:11.5px;line-height:21px}

/* header */
.site-header{left:0;top:0;width:1200px;height:74px;background:var(--white)}
.brand{left:62px;top:16px;font-weight:700;font-size:21px;line-height:22px;color:var(--teal);letter-spacing:.3px}
.call{left:745px;top:11px;display:flex;align-items:center;gap:10px}
.call-icon{width:50px;height:50px;border-radius:50%;background:#eaf6f4;display:flex;align-items:center;justify-content:center}
.call small{display:block;font-size:14px;color:var(--teal);line-height:16px}
.call strong{display:block;font-size:19px;color:var(--ink);font-weight:600;line-height:22px}
.btn-dark{background:var(--ink);color:#fff;font-weight:600;border-radius:30px;display:flex;align-items:center;justify-content:center;letter-spacing:.3px}
.header-btn{left:953px;top:19px;width:188px;height:37px;font-size:14px}

.main-nav{left:0;top:74px;width:1200px;height:42px;background:var(--teal)}
.main-nav ul{list-style:none;display:flex;height:42px;padding-left:62px}
.main-nav li{font-size:11.5px;font-weight:600;color:#fff;display:flex;align-items:center;padding:0 24px;letter-spacing:.2px}
.main-nav li.active{background:var(--teal-dark)}

/* hero */
.hero{left:0;top:116px;width:1200px;height:678px;overflow:hidden}
.hero-photo{position:absolute;inset:0;background:linear-gradient(90deg,#bfe4dc 0%,#a9d7c9 35%,#8fbf9d 55%,#c9a68c 72%,#7f8f7a 100%)}
.hero-photo::after{content:"";position:absolute;left:0;bottom:0;width:100%;height:260px;background:linear-gradient(180deg,rgba(90,140,90,0) 0%,rgba(70,130,80,.55) 100%)}
.hero-wave{position:absolute;left:0;bottom:0}
.hero h1{left:62px;top:166px;font-size:64px;line-height:72px;font-weight:800;color:var(--ink);letter-spacing:1px}
.hero .lead{left:62px;top:316px;width:520px;font-size:11.5px;line-height:21px;color:#333}
.hero-cta{left:60px;top:374px;display:flex;align-items:center}
.hero-cta .btn-dark{width:230px;height:45px;font-size:14.5px}
.or{width:36px;height:36px;border-radius:50%;background:#fff;color:var(--ink);font-weight:700;font-size:11px;display:flex;align-items:center;justify-content:center;margin:0 -18px;position:relative;z-index:2;border:3px solid var(--ink)}
.hero-call{width:240px;height:45px;border-radius:30px;background:var(--teal);color:#fff;font-size:14.5px;display:flex;align-items:center;justify-content:center;padding-left:14px}
.hero-call b{font-weight:600;margin-left:4px}

/* welcome */
.clinic-block{left:59px;top:851px;width:300px;height:224px;background:var(--teal)}
.clinic-photo{left:74px;top:867px;width:361px;height:300px;background:linear-gradient(135deg,#dfe7ee 0%,#b8c8d6 45%,#3b7fc0 100%)}
.dots{left:364px;top:1094px}
.eyebrow{font-size:11px;font-weight:600;letter-spacing:3px;color:var(--teal)}
.welcome-eyebrow{left:578px;top:850px}
.section-title{font-weight:700;color:var(--ink);letter-spacing:.5px}
.clinic-title{left:578px;top:866px;font-size:38px;line-height:46px}
.bar{height:3px;width:62px;background:var(--teal)}
.clinic-bar{left:578px;top:918px}
.clinic-text{left:578px;top:940px;width:450px}
.clinic-text p+p{margin-top:10px}
.btn-teal{background:var(--teal);color:#fff;border-radius:30px;font-weight:600;display:flex;align-items:center;justify-content:center}
.learn-btn{left:578px;top:1107px;width:164px;height:42px;font-size:14px}
.badges{left:582px;top:1170px;display:flex;gap:46px;align-items:center}
.badge-round{width:68px;height:64px;border-radius:50%;background:#e5e9ec;border:2px solid #c6ccd1}
.badge-wide{width:176px;height:62px;background:#f4e3e3;border-radius:6px}
.badge-sq{width:58px;height:62px;border-radius:50%;background:#fbefe0;border:2px solid #f0c58f}
.badge-text{width:90px;height:50px;background:#e3e7f3;border-radius:4px}

/* specialists */
.split-title{font-size:37px;line-height:43px;color:var(--ink)}
.split-title span{font-weight:300;display:block}
.split-title b{font-weight:700;letter-spacing:1px}
.spec-title{left:62px;top:1310px}
.spec-bar{left:62px;top:1412px}
.spec-text{left:405px;top:1312px;width:725px}
.cards{left:59px;top:1446px;display:flex;gap:31px}
.card{width:246px;height:455px;border:1px solid var(--line);background:#fff}
.card .photo{height:247px}
.card h3{font-size:14px;font-weight:700;color:var(--ink);margin:22px 0 0 17px;letter-spacing:.3px}
.card .degree{font-size:10.5px;color:var(--teal);margin-left:17px;line-height:16px}
.card p{font-size:10.5px;line-height:19px;margin:6px 17px 0;color:#555}
.card .btn-teal{width:182px;height:35px;font-size:11.5px;margin:14px 0 0 15px;letter-spacing:.3px}

/* therapy */
.therapy{left:0;top:1970px;width:1200px;height:374px}
.therapy h2{position:absolute;left:0;top:106px;width:1200px;text-align:center;font-size:36px;font-weight:300;color:#fff;letter-spacing:.5px}
.therapy h2 b{font-weight:700}
.therapy p{position:absolute;left:200px;top:170px;width:800px;text-align:center;color:#fff}
.therapy-form{position:absolute;left:168px;top:258px;display:flex;gap:17px}
.field{width:224px;height:40px;background:rgba(255,255,255,.22);border:1px solid rgba(255,255,255,.35);color:#fff;font-size:12px;display:flex;align-items:center;padding-left:12px}
.reach{width:142px;height:40px;background:#fff;color:var(--ink);font-size:12.5px;font-weight:600;display:flex;align-items:center;justify-content:center}

/* services */
.help-title{left:62px;top:2402px}
.help-bar{left:62px;top:2504px}
.help-text{left:405px;top:2404px;width:725px}
.service{width:220px;text-align:center}
.service svg{display:block;margin:0 auto}
.service h3{font-size:15px;font-weight:500;color:var(--ink);margin-top:12px}
.service p{font-size:10.5px;line-height:19px;color:var(--muted);margin-top:6px}
.book-box{left:891px;top:2748px;width:248px;height:183px;background:var(--teal);color:#fff;text-align:center;padding-top:34px}
.book-box h3{font-size:22px;line-height:29px;font-weight:700;letter-spacing:.5px}
.book-arrow{width:46px;height:46px;border-radius:50%;background:rgba(255,255,255,.25);margin:14px auto 0;display:flex;align-items:center;justify-content:center}

/* next step */
.next{left:0;top:2990px;width:1200px;height:660px}
.next h2{position:absolute;left:0;top:140px;width:1200px;text-align:center;font-size:37px;font-weight:400;color:var(--ink)}
.next h2 b{font-weight:700}
.next .bar{position:absolute;left:569px;top:198px}
.step{top:242px;width:337px;height:336px;background:#fff;border:8px solid #f7f7f7;text-align:center}
.step h3{font-size:13.5px;font-weight:700;color:var(--ink);letter-spacing:.3px;margin-top:14px}
.step svg{display:block;margin:0 auto}
.pill{width:248px;height:33px;border:1px solid #ccc;border-radius:20px;margin:0 auto;font-size:11px;color:#999;text-align:left;padding-left:16px;display:flex;align-items:center}
.step.loc{background:var(--teal);border-color:#7fd1c5}
.step.loc h3{color:#fff}
.map{width:293px;height:150px;margin:16px auto 0;background:linear-gradient(135deg,#d8e7c9 0%,#c9dcb6 40%,#e3d7b9 65%,#9fc6e6 100%)}

/* footer */
.footer{left:0;top:3600px;width:1200px;height:371px}
.footer h4{font-size:12.5px;font-weight:600;color:var(--teal);letter-spacing:.5px}
.footer .line{font-size:11px;color:#bbb;line-height:14px}
.footer-links{font-size:11px;color:#bbb}
.social{display:flex;gap:22px;align-items:center}
.social span{width:11px;height:11px;border-radius:50%;background:var(--teal);display:block}
.footer-brand{font-size:21px;font-weight:700;line-height:24px;color:var(--teal)}
.copyright{left:0;top:3941px;width:1200px;text-align:center;font-size:11px;color:#aaa}
.copyright span{color:var(--teal)}
</style>
</head>
<body>

<header class="abs site-header">
  <div class="abs brand">GREYFIELD RIDGE<br>MEDICAL</div>
  <div class="abs call">
    <div class="call-icon">
      <svg width="24" height="24" viewBox="0 0 24 24" fill="none" stroke="#1e1e1e" stroke-width="1.8"><path d="M5 3h4l2 5-2.5 1.5a11 11 0 0 0 6 6L16 13l5 2v4a2 2 0 0 1-2 2A17 17 0 0 1 3 5a2 2 0 0 1 2-2z"/></svg>
    </div>
    <div><small>CALL US</small><strong>123 456 7890</strong></div>
  </div>
  <div class="abs btn-dark header-btn">GET APPOINTMENT</div>
</header>

<nav class="abs main-nav">
  <ul>
    <li class="active">HOME</li><li>ABOUT US</li><li>OUR SERVICES</li><li>NEW PATIENTS</li><li>HEALTH PROFESSIONAL</li><li>ONLINE APPOINTMENT</li><li>CONTACT US</li>
  </ul>
</nav>

<section class="abs hero">
  <div class="hero-photo" role="img" aria-label="Smiling couple outdoors against a soft green park background"></div>
  <svg class="hero-wave" width="1200" height="120" viewBox="0 0 1200 120" preserveAspectRatio="none"><path d="M0 52 C 180 110 380 110 600 60 C 820 10 1000 30 1200 100 L1200 120 L0 120 Z" fill="#fff"/></svg>
  <h1 class="abs">LIVING HEALTH<br>MATTERS</h1>
  <p class="abs lead">Lorem Ipsum is simply dummy text of the printing and typesetting industry.<br>Lorem Ipsum has been the industry's standard dummy text.</p>
  <div class="abs hero-cta">
    <div class="btn-dark">GET APPOINTMENT</div>
    <div class="or">OR</div>
    <div class="hero-call">CALL US <b>+123 456 7890</b></div>
  </div>
</section>

<section class="welcome">
  <div class="abs clinic-block"></div>
  <div class="abs clinic-photo" role="img" aria-label="Bright clinic reception area with curved front desk"></div>
  <svg class="abs dots" width="112" height="112" viewBox="0 0 112 112" fill="#33b8a4">
    <g>
      <circle cx="80" cy="4" r="1.6"/><circle cx="96" cy="4" r="1.6"/><circle cx="80" cy="20" r="1.6"/><circle cx="96" cy="20" r="1.6"/><circle cx="80" cy="36" r="1.6"/><circle cx="96" cy="36" r="1.6"/><circle cx="80" cy="52" r="1.6"/><circle cx="96" cy="52" r="1.6"/>
      <circle cx="0" cy="76" r="1.6"/><circle cx="16" cy="76" r="1.6"/><circle cx="32" cy="76" r="1.6"/><circle cx="48" cy="76" r="1.6"/><circle cx="64" cy="76" r="1.6"/><circle cx="80" cy="76" r="1.6"/><circle cx="96" cy="76" r="1.6"/>
      <circle cx="0" cy="92" r="1.6"/><circle cx="16" cy="92" r="1.6"/><circle cx="32" cy="92" r="1.6"/><circle cx="48" cy="92" r="1.6"/><circle cx="64" cy="92" r="1.6"/><circle cx="80" cy="92" r="1.6"/><circle cx="96" cy="92" r="1.6"/>
      <circle cx="0" cy="108" r="1.6"/><circle cx="16" cy="108" r="1.6"/><circle cx="32" cy="108" r="1.6"/><circle cx="48" cy="108" r="1.6"/><circle cx="64" cy="108" r="1.6"/><circle cx="80" cy="108" r="1.6"/><circle cx="96" cy="108" r="1.6"/>
    </g>
  </svg>
  <div class="abs eyebrow welcome-eyebrow">WELCOME TO</div>
  <h2 class="abs section-title clinic-title">OUR CLINIC</h2>
  <div class="abs bar clinic-bar"></div>
  <div class="abs clinic-text">
    <p>Lorem Ipsum is simply dummy text of the printing and typesetting industry. Lorem Ipsum has been the industry's standard dummy text ever since the 1500s, when an unknown printer took a galley of type and scrambled it to make a type specimen book.</p>
    <p>Lorem Ipsum is simply dummy text of the printing and typesetting industry. Lorem Ipsum has been the industry.</p>
  </div>
  <div class="abs btn-teal learn-btn">LEARN MORE</div>
  <div class="abs badges" aria-label="Awards and memberships">
    <div class="badge-round"></div>
    <div class="badge-wide"></div>
    <div class="badge-sq"></div>
    <div class="badge-text"></div>
  </div>
</section>

<section class="specialists">
  <h2 class="abs split-title spec-title"><span>GET HELP FROM</span><b>A SPECIALIST</b></h2>
  <div class="abs bar spec-bar"></div>
  <p class="abs spec-text">Lorem Ipsum is simply dummy text of the printing and typesetting industry. Lorem Ipsum has been the industry's standard dummy text ever since the 1500s, when an unknown printer took a galley of type and scrambled it to make a type specimen book.Lorem Ipsum is simply dummy text of the printing and typesetting industry. Lorem Ipsum has been the industry.</p>
  <div class="abs cards">
    <article class="card">
      <div class="photo" role="img" aria-label="Portrait of a specialist in a light blazer" style="background:linear-gradient(160deg,#f1ece6,#d9cfc4)"></div>
      <h3>SPECIALIST NAME</h3><div class="degree">Specialist Degree</div>
      <p>Lorem Ipsum is simply dummy text of the printing and typesetting industry. Lorem Ipsum has been the industry...</p>
      <div class="btn-teal">BOOK AN APPOINTMENT</div>
    </article>
    <article class="card">
      <div class="photo" role="img" aria-label="Portrait of a doctor wearing a mask and stethoscope" style="background:linear-gradient(160deg,#b9c7b0,#e9ebe8)"></div>
      <h3>SPECIALIST NAME</h3><div class="degree">Specialist Degree</div>
      <p>Lorem Ipsum is simply dummy text of the printing and typesetting industry. Lorem Ipsum has been the industry...</p>
      <div class="btn-teal">BOOK AN APPOINTMENT</div>
    </article>
    <article class="card">
      <div class="photo" role="img" aria-label="Portrait of a doctor in a white coat outdoors" style="background:linear-gradient(160deg,#6f8f52,#dfe2dc)"></div>
      <h3>SPECIALIST NAME</h3><div class="degree">Specialist Degree</div>
      <p>Lorem Ipsum is simply dummy text of the printing and typesetting industry. Lorem Ipsum has been the industry...</p>
      <div class="btn-teal">BOOK AN APPOINTMENT</div>
    </article>
    <article class="card">
      <div class="photo" role="img" aria-label="Portrait of a specialist against a pink backdrop" style="background:linear-gradient(160deg,#e2648a,#f0d9dc)"></div>
      <h3>SPECIALIST NAME</h3><div class="degree">Specialist Degree</div>
      <p>Lorem Ipsum is simply dummy text of the printing and typesetting industry. Lorem Ipsum has been the industry...</p>
      <div class="btn-teal">BOOK AN APPOINTMENT</div>
    </article>
  </div>
</section>

<section class="abs therapy">
  <svg class="abs" style="left:0;top:0" width="1200" height="374" viewBox="0 0 1200 374" preserveAspectRatio="none">
    <defs><linearGradient id="therapyFill" x1="0" y1="0" x2="0" y2="1"><stop offset="0" stop-color="#86cfc6"/><stop offset="1" stop-color="#33b8a4"/></linearGradient></defs>
    <path d="M0 40 C 200 80 420 60 620 20 C 800 -8 1000 10 1200 45 L1200 374 L0 374 Z" fill="url(#therapyFill)"/>
  </svg>
  <h2>TRY ONLINE <b>THERAPY</b></h2>
  <p>Lorem Ipsum is simply dummy text of the printing and typesetting industry. Lorem Ipsum has been the industry's standard dummy text ever since the 1500s, when an unknown printer took a galley.</p>
  <div class="therapy-form">
    <div class="field">Name</div><div class="field">Email</div><div class="field">Phone</div><div class="reach">REACH OUT</div>
  </div>
</section>

<section class="services">
  <h2 class="abs split-title help-title"><span>IT'S OK TO</span><b>ASK FOR HELP</b></h2>
  <div class="abs bar help-bar"></div>
  <p class="abs help-text">Lorem Ipsum is simply dummy text of the printing and typesetting industry. Lorem Ipsum has been the industry's standard dummy text ever since the 1500s, when an unknown printer took a galley of type and scrambled it to make a type specimen book.Lorem Ipsum is simply dummy text of the printing and typesetting industry. Lorem Ipsum has been the industry.</p>

  <div class="abs service" style="left:75px;top:2537px">
    <svg width="50" height="50" viewBox="0 0 50 50" fill="none" stroke="#33b8a4" stroke-width="1.8"><path d="M25 40 C10 30 6 22 6 16 a9 9 0 0 1 19-3 a9 9 0 0 1 19 3 c0 6-4 14-19 24z"/><path d="M14 22h6l3-5 4 9 3-4h6"/></svg>
    <h3>General Practice</h3><p>Lorem Ipsum has been the industry's standard dummy text ever since the when an unknown printer.</p>
  </div>
  <div class="abs service" style="left:351px;top:2537px">
    <svg width="50" height="50" viewBox="0 0 50 50" fill="none" stroke="#33b8a4" stroke-width="1.8"><circle cx="25" cy="25" r="11"/><path d="M25 4v10M25 36v10M4 25h10M36 25h10M10 10l7 7M33 33l7 7M40 10l-7 7M17 33l-7 7"/><circle cx="22" cy="22" r="2"/><circle cx="29" cy="28" r="2"/></svg>
    <h3>Covid-19 Service</h3><p>Lorem Ipsum has been the industry's standard dummy text ever since the when an unknown printer.</p>
  </div>
  <div class="abs service" style="left:629px;top:2537px">
    <svg width="50" height="50" viewBox="0 0 50 50" fill="none" stroke="#33b8a4" stroke-width="1.8"><path d="M14 8 l6 20 h14 l4 8 H16"/><path d="M20 36v8M32 36v8M12 44h28"/><circle cx="14" cy="8" r="3"/><path d="M30 10h10v8H30z"/></svg>
    <h3>Dentists</h3><p>Lorem Ipsum has been the industry's standard dummy text ever since the when an unknown printer.</p>
  </div>
  <div class="abs service" style="left:905px;top:2537px">
    <svg width="50" height="50" viewBox="0 0 50 50" fill="none" stroke="#33b8a4" stroke-width="1.8"><rect x="18" y="4" width="14" height="6" rx="3"/><rect x="18" y="13" width="14" height="6" rx="3"/><rect x="18" y="22" width="14" height="6" rx="3"/><path d="M6 20c0 14 8 22 14 24M44 20c0 14-8 22-14 24"/></svg>
    <h3>Phsiotherapy</h3><p>Lorem Ipsum has been the industry's standard dummy text ever since the when an unknown printer.</p>
  </div>
  <div class="abs service" style="left:75px;top:2747px">
    <svg width="50" height="50" viewBox="0 0 50 50" fill="none" stroke="#33b8a4" stroke-width="1.8"><circle cx="25" cy="16" r="9"/><path d="M8 46c0-10 8-16 17-16s17 6 17 16"/><circle cx="14" cy="38" r="2"/><circle cx="36" cy="38" r="2"/></svg>
    <h3>Dermatology</h3><p>Lorem Ipsum has been the industry's standard dummy text ever since the when an unknown printer.</p>
  </div>
  <div class="abs service" style="left:351px;top:2747px">
    <svg width="50" height="50" viewBox="0 0 50 50" fill="none" stroke="#33b8a4" stroke-width="1.8"><path d="M30 4v28c0 6-4 10-10 10H8c-3 0-4-3-2-5 3-3 8-4 12-6 4-2 6-5 6-9V4"/></svg>
    <h3>Podiatry</h3><p>Lorem Ipsum has been the industry's standard dummy text ever since the when an unknown printer.</p>
  </div>
  <div class="abs service" style="left:629px;top:2747px">
    <svg width="50" height="50" viewBox="0 0 50 50" fill="none" stroke="#33b8a4" stroke-width="1.8"><path d="M25 4v42"/><path d="M20 10h10M19 17h12M18 24h14M19 31h12M20 38h10"/><path d="M12 14c-4 6-4 16 0 22M38 14c4 6 4 16 0 22"/></svg>
    <h3>Chriopractic</h3><p>Lorem Ipsum has been the industry's standard dummy text ever since the when an unknown printer.</p>
  </div>
  <div class="abs book-box">
    <h3>BOOK AN<br>APPOINTMENT</h3>
    <div class="book-arrow"><svg width="18" height="18" viewBox="0 0 18 18" fill="none" stroke="#fff" stroke-width="1.8"><path d="M2 9h13M10 4l5 5-5 5"/></svg></div>
  </div>
</section>

<section class="abs next">
  <svg class="abs" style="left:0;top:0" width="1200" height="660" viewBox="0 0 1200 660" preserveAspectRatio="none">
    <path d="M0 32 C 220 60 400 80 620 40 C 820 5 1000 0 1200 30 L1200 660 L0 660 Z" fill="#efefef"/>
  </svg>
  <h2>TAKE <b>THE NEXT STEP</b></h2>
  <div class="bar"></div>

  <div class="abs step" style="left:60px">
    <svg width="62" height="50" viewBox="0 0 62 50" fill="none" stroke="#33b8a4" stroke-width="2" style="margin-top:58px"><rect x="2" y="4" width="58" height="42"/><path d="M2 4l29 24 29-24M2 46l22-20M60 46L38 26"/></svg>
    <h3>GET OUR NEWSLETTER</h3>
    <div class="pill" style="margin-top:22px">Name</div>
    <div class="pill" style="margin-top:12px">Email</div>
    <div class="btn-teal" style="width:248px;height:34px;margin:12px auto 0;font-size:13px">SUBSCRIBE</div>
  </div>

  <div class="abs step loc" style="left:431px">
    <svg width="30" height="44" viewBox="0 0 30 44" fill="none" stroke="#fff" stroke-width="2" style="margin-top:56px"><path d="M15 42S3 26 3 15a12 12 0 0 1 24 0c0 11-12 27-12 27z"/><circle cx="15" cy="15" r="5"/></svg>
    <h3>OUR LOCATION</h3>
    <div class="map" role="img" aria-label="Map showing the clinic location"></div>
  </div>

  <div class="abs step" style="left:802px">
    <svg width="46" height="46" viewBox="0 0 46 46" fill="none" stroke="#33b8a4" stroke-width="2" style="margin-top:60px"><rect x="3" y="7" width="40" height="36" rx="2"/><path d="M3 16h40M12 3v8M23 3v8M34 3v8"/><g fill="#33b8a4" stroke="none"><circle cx="12" cy="24" r="1.6"/><circle cx="20" cy="24" r="1.6"/><circle cx="28" cy="24" r="1.6"/><circle cx="36" cy="24" r="1.6"/><circle cx="12" cy="31" r="1.6"/><circle cx="20" cy="31" r="1.6"/><circle cx="28" cy="31" r="1.6"/><circle cx="36" cy="31" r="1.6"/><circle cx="12" cy="37" r="1.6"/><circle cx="20" cy="37" r="1.6"/></g></svg>
    <h3>BOOK A FREE CONSULT</h3>
    <p style="font-size:10.5px;line-height:20px;color:#999;width:260px;margin:12px auto 0">Lorem Ipsum has been the industry's standard dummy text ever since the when.</p>
    <div class="btn-teal" style="width:146px;height:34px;margin:14px auto 0;font-size:11.5px">SCHEDULE NOW</div>
    <div style="display:flex;align-items:center;justify-content:center;gap:10px;margin-top:12px;font-size:19px;font-weight:600;color:#1e1e1e">
      <svg width="22" height="22" viewBox="0 0 24 24" fill="none" stroke="#1e1e1e" stroke-width="1.8"><path d="M5 3h4l2 5-2.5 1.5a11 11 0 0 0 6 6L16 13l5 2v4a2 2 0 0 1-2 2A17 17 0 0 1 3 5a2 2 0 0 1 2-2z"/></svg>
      123 456 7890
    </div>
  </div>
</section>

<footer class="abs footer">
  <svg class="abs" style="left:0;top:0" width="1200" height="371" viewBox="0 0 1200 371" preserveAspectRatio="none">
    <path d="M0 14 C 260 70 480 110 640 104 C 820 96 1000 50 1200 30 L1200 371 L0 371 Z" fill="#1e1e1e"/>
  </svg>
  <h4 class="abs" style="left:62px;top:142px">CONTACT INFO</h4>
  <div class="abs line" style="left:62px;top:181px">Call Us : 123 456 7890</div>
  <div class="abs line" style="left:62px;top:219px">Email Us : info@greyfieldridgemedical.com</div>
  <div class="abs line" style="left:62px;top:257px">Address : Lorem Ipsum is simply dummy text and printing.</div>

  <h4 class="abs" style="left:432px;top:142px">QUICK LINKS</h4>
  <div class="abs footer-links" style="left:432px;top:181px;line-height:30.5px">
    <span style="color:var(--teal)">Home</span><br>About Us<br>Our Services<br>New Patients
  </div>
  <div class="abs footer-links" style="left:604px;top:181px;line-height:30.5px">
    Health Professional<br>Online Appointment<br>Contact
  </div>

  <h4 class="abs" style="left:803px;top:142px">FOLLOW US</h4>
  <div class="abs social" style="left:803px;top:182px" aria-label="Social media links">
    <span></span><span></span><span></span><span></span><span></span>
  </div>
  <div class="abs footer-brand" style="left:803px;top:236px">GREYFIELD RIDGE<br>MEDICAL</div>
</footer>
<div class="abs copyright">© <span>Greyfield Ridge Medical</span> - 2020. All Rights Reserved.</div>

</body>
</html>
```